Looking for a creative label design for our retail coffee bags

We are a coffee manufacturer (coffee roaster) looking to re-brand our retail label for our coffee bags. Our main coffee blend that we sell is our Harborline Velvet Blend. You can use this name when creating the label. We are going for a look that represents our company as a coffee roaster. Please reference our website (www.brindlemugworks.com) and our Facebook page to learn more about our company and to give you more inspiration on creating this design.

Target Market(s)

Retail customers/grocery stores

Industry/Entity Type

Manufacturer

Requirements
Must have
• The size of the label has to be 3" width x 4" height

Logo must be Black
Nice to have
• We currently incorporate a color on our labels for each blend. For example, Harborline Velvet Blend (royal blue), Decaffeinated Blend (red), Breakfast Blend (green), Flavored coffees (gold).

Rustic/vintage style

```html
<!DOCTYPE html>
<html lang="en">
<head>
<meta charset="utf-8">
<title>Brindle Mug Coffee – Harborline Velvet Blend Label</title>
<link rel="stylesheet" href="https://fonts.googleapis.com/css2?family=Barlow+Condensed:wght@600;800&family=Barlow:wght@400;500&display=swap">
<style>
  :root {
    --page-bg: #f4f1ec;
    --label-dark: #1c1c1c;
    --label-mid: #4a4a4a;
    --label-light: #7a7a7a;
    --badge-white: #f7f7f5;
    --ink-black: #121212;
    --blend-red: #b81f2b;
    --text-light: #f2f2f2;
  }
  * { margin: 0; padding: 0; box-sizing: border-box; }
  html, body {
    width: 1200px;
    height: 950px;
    overflow: hidden;
    background: var(--page-bg);
  }
  .canvas {
    position: relative;
    width: 1200px;
    height: 950px;
  }
  .label {
    position: absolute;
    left: 300px;
    top: 75px;
    width: 600px;
    height: 800px;
    overflow: hidden;
    background: var(--label-dark);
  }
  .label-photo {
    position: absolute;
    inset: 0;
    background:
      radial-gradient(ellipse at 75% 20%, var(--label-light) 0%, transparent 35%),
      radial-gradient(ellipse at 30% 70%, var(--label-mid) 0%, transparent 55%),
      linear-gradient(160deg, #2a2a2a 0%, #3c3c3c 45%, #1a1a1a 100%);
  }
  .brand-badge {
    position: absolute;
    left: 97px;
    top: 118px;
    width: 406px;
    height: 406px;
    border-radius: 50%;
    background: var(--badge-white);
    display: flex;
    flex-direction: column;
    align-items: center;
    justify-content: center;
    text-align: center;
  }
  .brand-name {
    font-family: "Barlow Condensed", sans-serif;
    font-weight: 800;
    color: var(--ink-black);
    text-transform: uppercase;
    font-size: 84px;
    line-height: 0.92;
    letter-spacing: 1px;
  }
  .brand-tagline {
    margin-top: 22px;
    font-family: "Barlow Condensed", sans-serif;
    font-weight: 600;
    font-size: 13px;
    letter-spacing: 1.5px;
    text-transform: uppercase;
    color: var(--ink-black);
  }
  .blend-band {
    position: absolute;
    left: 105px;
    top: 583px;
    width: 403px;
    height: 46px;
    background: var(--blend-red);
    color: var(--text-light);
    font-family: "Barlow Condensed", sans-serif;
    font-weight: 600;
    font-size: 24px;
    letter-spacing: 1.5px;
    text-transform: uppercase;
    display: flex;
    align-items: center;
    justify-content: center;
  }
  .blend-description {
    position: absolute;
    left: 60px;
    top: 648px;
    width: 480px;
    font-family: "Barlow", sans-serif;
    font-weight: 400;
    font-size: 14.5px;
    line-height: 1.5;
    color: var(--text-light);
    text-align: center;
  }
  .spec-row {
    position: absolute;
    left: 0;
    top: 718px;
    width: 600px;
    display: flex;
    justify-content: center;
    font-family: "Barlow", sans-serif;
    font-weight: 400;
    font-size: 18px;
    line-height: 1.2;
    color: var(--text-light);
    text-align: center;
  }
  .spec-item {
    padding: 0 22px;
  }
  .spec-item + .spec-item {
    border-left: 3px solid var(--text-light);
  }
</style>
</head>
<body>
  <main class="canvas">
    <section class="label">
      <div class="label-photo" role="img" aria-label="Black and white photo of dark roasted coffee beans tumbling in a roaster drum"></div>

      <div class="brand-badge">
        <div class="brand-name">Brindle<br>Mug<br>Coffee</div>
        <div class="brand-tagline">Proudly roasted in Millbrook, OH since 1994.</div>
      </div>

      <div class="blend-band">Harborline Velvet Blend</div>

      <p class="blend-description">Made from the best Arabica beans South America has to offer, carefully roasted to perfection.&nbsp; A distinctive rich aroma with a smooth undertones.</p>

      <div class="spec-row">
        <div class="spec-item">WHOLE<br>BEAN</div>
        <div class="spec-item">DARK<br>ROAST</div>
        <div class="spec-item">2LB<br>NET</div>
      </div>
    </section>
  </main>
</body>
</html>
```